Automotive lighting company needs professional business card

Hello, we are an automotive lighting company and looking to have a professional business card designed for us. We have included some images which can be used on the card. Website is www.brightlanemotorparts.example which has all of our details on it. Email is brightlanemotorparts@mailbox.example phone number is 1300 862 317 thank you guys!

Target Market(s)

Automotive industry

Contact Information for Business Card

Phone - 1300 862 317
Web - www.brightlanemotorparts.example
Email - brightlanemotorparts@mailbox.example

Requirements
Must have
• Looking to have a dark theme. Elegant and professional. Needs to look and feel like a high quality card to represent high quality company.

```html
<!DOCTYPE html>
<html lang="en">
<head>
<meta charset="utf-8">
<title>Brightlane Motor Parts — Business Card</title>
<link rel="stylesheet" href="https://fonts.googleapis.com/css2?family=Lato:wght@400;700&family=Michroma&display=swap">
<style>
  :root {
    --stage: #e9e9e7;
    --charcoal: #333335;
    --brand-blue: #1b8fd0;
    --paper: #ffffff;
    --ink: #3a3a3c;
    --rule: #d9d9d9;
  }
  * { box-sizing: border-box; margin: 0; padding: 0; }
  html, body {
    width: 1200px;
    height: 900px;
    overflow: hidden;
    background: var(--stage);
  }
  .stage {
    position: relative;
    width: 1200px;
    height: 900px;
  }
  .card {
    position: absolute;
    width: 560px;
    height: 342px;
    overflow: hidden;
    box-shadow: 0 10px 28px rgba(0, 0, 0, 0.18);
  }

  /* Shared wordmark */
  .wordmark {
    position: absolute;
    display: flex;
    align-items: center;
  }
  .wordmark__dot {
    flex: none;
    border-radius: 50%;
    background: var(--brand-blue);
  }
  .wordmark__name {
    font-family: "Michroma", sans-serif;
    color: var(--brand-blue);
    white-space: nowrap;
    line-height: 1.35;
  }
  .wordmark__line { display: block; }

  /* Back of card */
  .card--back {
    left: 90px;
    top: 100px;
    background: var(--charcoal);
  }
  .card--back .wordmark {
    left: 0;
    right: 0;
    top: 110px;
    justify-content: center;
    gap: 14px;
  }
  .card--back .wordmark__dot { width: 18px; height: 18px; }
  .card--back .wordmark__name {
    font-size: 22px;
    letter-spacing: 1px;
    text-align: left;
  }
  .card--back .wordmark-rule {
    position: absolute;
    left: 150px;
    right: 150px;
    top: 190px;
    height: 1px;
    background: var(--rule);
  }
  .card--back .web {
    position: absolute;
    left: 0;
    right: 0;
    top: 256px;
    text-align: center;
    font-family: "Lato", sans-serif;
    font-size: 14px;
    color: var(--paper);
  }

  /* Front of card */
  .card--front {
    left: 550px;
    top: 470px;
    background: var(--paper);
  }
  .card--front .wave {
    position: absolute;
    inset: 0;
  }
  .person {
    position: absolute;
    left: 36px;
    top: 48px;
  }
  .person__name {
    font-family: "Michroma", sans-serif;
    font-size: 15px;
    font-weight: 400;
    letter-spacing: 1px;
    color: var(--brand-blue);
    white-space: nowrap;
  }
  .person__role {
    font-family: "Lato", sans-serif;
    font-size: 15px;
    color: var(--ink);
    margin-top: 2px;
  }
  .card--front .wordmark {
    right: 36px;
    top: 50px;
    gap: 10px;
  }
  .card--front .wordmark__dot { width: 12px; height: 12px; }
  .card--front .wordmark__name {
    font-size: 14px;
    letter-spacing: 0.5px;
    text-align: right;
  }
  .card--front .wordmark-rule {
    position: absolute;
    right: 36px;
    top: 100px;
    width: 190px;
    height: 1px;
    background: var(--rule);
  }
  .contact {
    position: absolute;
    left: 36px;
    top: 166px;
    list-style: none;
    font-family: "Lato", sans-serif;
    font-size: 16px;
    color: var(--ink);
  }
  .contact li {
    display: flex;
    align-items: center;
    gap: 8px;
    line-height: 26px;
    white-space: nowrap;
  }
  .contact svg { width: 15px; height: 15px; fill: var(--brand-blue); }
  .card--front .web {
    position: absolute;
    right: 26px;
    top: 262px;
    font-family: "Lato", sans-serif;
    font-size: 13px;
    color: var(--paper);
    white-space: nowrap;
  }
</style>
</head>
<body>
<main class="stage">

  <section class="card card--back" aria-label="Business card, back">
    <div class="wordmark">
      <span class="wordmark__dot"></span>
      <span class="wordmark__name">
        <span class="wordmark__line">BRIGHTLANE</span>
        <span class="wordmark__line">MOTOR PARTS</span>
      </span>
    </div>
    <div class="wordmark-rule"></div>
    <p class="web">www.brightlanemotorparts.example</p>
  </section>

  <section class="card card--front" aria-label="Business card, front">
    <svg class="wave" viewBox="0 0 560 342" preserveAspectRatio="none" aria-hidden="true">
      <path d="M0,312 C190,330 390,250 560,112 L560,342 L0,342 Z" fill="var(--charcoal)"/>
      <path d="M0,274 C170,312 340,262 460,190 C350,276 180,318 0,298 Z" fill="var(--brand-blue)"/>
    </svg>

    <div class="person">
      <h1 class="person__name">DANIEL HARPER</h1>
      <p class="person__role">Managing Director</p>
    </div>

    <div class="wordmark">
      <span class="wordmark__dot"></span>
      <span class="wordmark__name">
        <span class="wordmark__line">BRIGHTLANE</span>
        <span class="wordmark__line">MOTOR PARTS</span>
      </span>
    </div>
    <div class="wordmark-rule"></div>

    <ul class="contact">
      <li>
        <svg viewBox="0 0 24 24" aria-hidden="true"><path d="M6.6 10.8a15.1 15.1 0 0 0 6.6 6.6l2.2-2.2a1 1 0 0 1 1-.25 11.4 11.4 0 0 0 3.6.57 1 1 0 0 1 1 1V20a1 1 0 0 1-1 1A17 17 0 0 1 3 4a1 1 0 0 1 1-1h3.5a1 1 0 0 1 1 1c0 1.25.2 2.45.57 3.57a1 1 0 0 1-.25 1z"/></svg>
        1300 862 317
      </li>
      <li>
        <svg viewBox="0 0 24 24" aria-hidden="true"><path d="M2 5h20v14H2z M2 5l10 8 10-8" fill="var(--brand-blue)" stroke="#fff" stroke-width="1.4"/></svg>
        brightlanemotorparts@mailbox.example
      </li>
    </ul>

    <p class="web">www.brightlanemotorparts.example</p>
  </section>

</main>
</body>
</html>
```